"Unwind & Depart" Book Cover 5.5x8.5

Title of the book is "Unwind & Depart"
Subtitle is "Charting Quiet Harbors"
I've used PixelGuild on multiple occasions you can look on my Brindle page, Mark Oberfeld, to see the covers I've used in the other projects I've done.
The target audience are people who have been tricked to think they can't retire because inflation, i.e. cost of living is going up so much they must work to keep up. There is no evidence of this.
And those are the people I want to reach so they can "Unwind...and Depart."
Target Market(s)
Americans aged 55 and over who are thinking about retirement
Industry/Entity Type
Financial
Requirements
Nice to have
- Keep It Simple, Stupid is my mantra. Just make it pop out when people are browsing
Should not have
- No piggy banks. No old people sitting on a beach.

```html
<!DOCTYPE html>
<html lang="en">
<head>
<meta charset="utf-8">
<title>Unwind &amp; Depart — Book Cover</title>
<link href="https://fonts.googleapis.com/css2?family=Bebas+Neue&family=Montserrat:wght@700&family=Oswald:wght@500&display=swap" rel="stylesheet">
<style>
  :root {
    --page-bg: #ffffff;
    --cover-bg: #ffffff;
    --ink-slate: #233a44;
    --teal-deep: #0c4558;
    --teal-mid: #1f7687;
    --teal-light: #2d8f9c;
    --sea-blue: #3d9fd0;
    --sea-pale: #cfe6f2;
    --wicker-tan: #c9a764;
    --wicker-dark: #7c6a4a;
    --band-text: #ffffff;
  }
  * { margin: 0; padding: 0; box-sizing: border-box; }
  html, body {
    width: 1200px;
    height: 1000px;
    overflow: hidden;
    background: var(--page-bg);
  }
  .book-cover {
    position: absolute;
    left: 348px;
    top: 110px;
    width: 505px;
    height: 780px;
    background: var(--cover-bg);
    overflow: hidden;
  }
  .cover-scene {
    position: absolute;
    left: 0;
    top: 360px;
    width: 505px;
    height: 340px;
    background:
      linear-gradient(180deg, rgba(255,255,255,1) 0%, rgba(255,255,255,0.55) 18%, rgba(255,255,255,0) 38%),
      linear-gradient(180deg, var(--sea-pale) 0%, var(--sea-blue) 40%, #5aa7c9 58%, var(--wicker-tan) 72%, var(--wicker-dark) 100%);
  }
  .cover-title {
    position: absolute;
    left: 0;
    top: 0;
    width: 505px;
    height: 700px;
  }
  .subtitle {
    font-family: "Montserrat", sans-serif;
    font-weight: 700;
    font-size: 20px;
    letter-spacing: 1.6px;
    fill: var(--ink-slate);
  }
  .title-word {
    font-family: "Bebas Neue", sans-serif;
    font-size: 196px;
  }
  .title-joiner {
    font-family: "Montserrat", sans-serif;
    font-weight: 700;
    font-size: 30px;
    letter-spacing: 9px;
    fill: var(--teal-mid);
  }
  .author-band {
    position: absolute;
    left: 0;
    top: 700px;
    width: 505px;
    height: 80px;
    background: linear-gradient(90deg, var(--teal-deep) 0%, var(--teal-light) 50%, var(--teal-deep) 100%);
    display: flex;
    align-items: center;
    justify-content: center;
  }
  .author-name {
    font-family: "Oswald", sans-serif;
    font-weight: 500;
    font-size: 40px;
    letter-spacing: 6px;
    color: var(--band-text);
    line-height: 1;
  }
</style>
</head>
<body>
  <main class="book-cover">
    <div class="cover-scene" role="img" aria-label="Photograph of a cup of coffee on a woven placemat overlooking a sunny harbour full of boats"></div>

    <svg class="cover-title" viewBox="0 0 505 700" xmlns="http://www.w3.org/2000/svg" aria-label="Unwind and Depart">
      <defs>
        <radialGradient id="titleTeal" cx="0.5" cy="0.4" r="0.6">
          <stop offset="0" stop-color="#2f8f9d"/>
          <stop offset="1" stop-color="#0c4558"/>
        </radialGradient>
      </defs>
      <text class="subtitle" x="252.5" y="60" text-anchor="middle" textLength="392" lengthAdjust="spacingAndGlyphs">CHARTING QUIET HARBORS</text>

      <text class="title-word" x="252.5" y="231" text-anchor="middle" fill="url(#titleTeal)" textLength="388" lengthAdjust="spacingAndGlyphs">UNWIND</text>

      <line x1="62" y1="259" x2="168" y2="259" stroke="var(--teal-deep)" stroke-width="3"/>
      <text class="title-joiner" x="256" y="270" text-anchor="middle">AND</text>
      <line x1="340" y1="259" x2="452" y2="259" stroke="var(--teal-deep)" stroke-width="3"/>

      <text class="title-word" x="252.5" y="421" text-anchor="middle" fill="url(#titleTeal)" textLength="390" lengthAdjust="spacingAndGlyphs">DEPART</text>
    </svg>

    <footer class="author-band">
      <span class="author-name">MARK OBERFELD</span>
    </footer>
  </main>
</body>
</html>
```